Acupuncture Medspa needs a business card design

I need a business card design that looks professional, has a spa-like quality and can offer a promo on the back. Initial promo is "First session free". The tagline of PinaVell is: Unwind, Mend, Glow.

PinaVell is a membership-based acupuncture medspa that offers acupuncture, cupping, and herbal therapies. Members choose between the "Refresh" membership which is for stress relief, or "Restore" which is for treating health conditions, and lastly "Rejuvenate" which is for natural facial enhancement.

Industry/Entity Type

Health And Wellness

Contact Information for Business Card

Doris Kettle, MAC, L.Ac.
614-385-2097
www.pinavell-example.com

Font styles to use
Serif
Sans Serif

Colors

Designer to choose colors to be used in the design.

Requirements
Must have
• The project must have PinaVell logo, promo on the back, and contact information
Nice to have
• I would like to see the colors of the logo used.

```html
<!DOCTYPE html>
<html lang="en">
<head>
<meta charset="utf-8">
<title>PinaVell Business Card</title>
<link rel="stylesheet" href="https://fonts.googleapis.com/css2?family=Montserrat:wght@600;700&family=Nunito+Sans:wght@300;400&display=swap">
<style>
  :root {
    --teal: #1a8883;
    --teal-soft: #3f9a95;
    --white: #ffffff;
    --ink: #3b2a24;
    --page: #ffffff;
  }
  html, body {
    margin: 0;
    padding: 0;
    width: 1000px;
    height: 1200px;
    overflow: hidden;
    background: var(--page);
  }
  .sheet { display: block; width: 1000px; height: 1200px; }
  .tagline { font-family: "Nunito Sans", sans-serif; font-weight: 300; fill: var(--white); }
  .brand-name { font-family: "Montserrat", sans-serif; font-weight: 600; letter-spacing: 1px; }
  .brand-name--front { fill: var(--teal); }
  .brand-name--back { fill: var(--white); }
  .holder-name { font-family: "Montserrat", sans-serif; font-weight: 700; fill: var(--teal); }
  .contact-text { font-family: "Montserrat", sans-serif; font-weight: 700; fill: var(--ink); }
  .promo { font-family: "Nunito Sans", sans-serif; font-weight: 400; fill: var(--white); letter-spacing: 5px; }
</style>
</head>
<body>
<svg class="sheet" viewBox="0 0 1000 1200" xmlns="http://www.w3.org/2000/svg">
  <defs>
    <radialGradient id="back-glow" cx="0.5" cy="0.45" r="0.6">
      <stop offset="0" stop-color="var(--teal-soft)" stop-opacity="0.55"/>
      <stop offset="1" stop-color="var(--teal)" stop-opacity="0"/>
    </radialGradient>
  </defs>

  <!-- Front side -->
  <g class="card card--front">
    <rect x="169.5" y="130.5" width="661" height="428" fill="var(--white)" stroke="var(--teal)" stroke-width="1"/>
    <rect class="header-band" x="170" y="160" width="660" height="88" fill="var(--teal)"/>
    <circle class="header-badge" cx="311" cy="203" r="66" fill="var(--white)"/>
    <text class="tagline" x="430" y="216" font-size="26">Unwind. Mend. Glow</text>

    <g class="brand brand--front">
      <circle cx="482" cy="325" r="9" fill="var(--teal)"/>
      <text class="brand-name brand-name--front" x="500" y="339" font-size="38">PINAVELL</text>
    </g>

    <text class="holder-name" x="205" y="417" font-size="20">Doris Kettle, MAC, L.Ac.</text>

    <g class="contact contact--phone">
      <path d="M215 456c-2 2-1 7 3 12s9 8 12 7l2-3-4-4-3 2c-2-1-5-4-6-6l2-3-3-4z" fill="var(--teal)"/>
      <path d="M224 455a8 8 0 0 1 7 7M225 450a13 13 0 0 1 11 12" fill="none" stroke="var(--teal)" stroke-width="1.6"/>
      <text class="contact-text" x="248" y="471" font-size="17" letter-spacing="2.5">614-385-2097</text>
    </g>
    <g class="contact contact--web">
      <rect x="215" y="486" width="20" height="13" fill="none" stroke="var(--teal)" stroke-width="1.8"/>
      <path d="M215 486l10 8 10-8M215 499l7-6M235 499l-7-6" fill="none" stroke="var(--teal)" stroke-width="1.5"/>
      <text class="contact-text" x="242" y="498" font-size="17">www.pinavell-example.com</text>
    </g>
  </g>

  <!-- Back side -->
  <g class="card card--back">
    <rect x="169" y="641" width="662" height="428" fill="var(--teal)"/>
    <rect x="169" y="641" width="662" height="428" fill="url(#back-glow)" role="img" aria-label="Faint large leaf decoration in soft teal"/>
    <g class="brand brand--back">
      <circle cx="307" cy="848" r="10" fill="var(--white)"/>
      <text class="brand-name brand-name--back" x="510" y="866" font-size="48" text-anchor="middle">PINAVELL</text>
    </g>
    <text class="tagline" x="500" y="905" font-size="26" text-anchor="middle">Unwind. Mend. Glow</text>
    <text class="promo" x="500" y="1043" font-size="21" text-anchor="middle">First Session Free</text>
  </g>
</svg>
</body>
</html>
```